Flyer for the Lumen 2025 Conference

I am looking to produce a flyer for our upcoming conference, Lumen 2025. This is an annual conference that we plan to publicize on social media. The ideal designer will create a flyer that is eye-catching and effectively communicates the key information. Please see attached our logo, speaker photo, and flyer content.

Target Market(s)

All demographics

Industry/Entity Type

Christian

Font styles to use
Sans Serif

Requirements
Should not have
• Cross, church

```html
<!DOCTYPE html>
<html lang="en">
<head>
<meta charset="utf-8">
<title>Lumen 2025 Conference</title>
<link rel="stylesheet" href="https://fonts.googleapis.com/css2?family=Oswald:wght@600;700&family=Barlow+Condensed:wght@800&family=Outfit:wght@400;600&display=swap">
<style>
  :root {
    --navy: #1c263c;
    --navy-deep: #141a36;
    --sky: #4bc4ea;
    --orange: #f7931e;
    --bar: #0b5598;
    --white: #ffffff;
    --ink: #0f2a5a;
  }
  * { box-sizing: border-box; margin: 0; padding: 0; }
  html, body { width: 895px; height: 1200px; overflow: hidden; }
  body { background: var(--navy); font-family: "Outfit", sans-serif; color: var(--white); }
  .flyer {
    position: relative; width: 895px; height: 1200px; overflow: hidden;
    background: radial-gradient(ellipse at 70% 40%, #26324d 0%, var(--navy) 55%, #171f33 100%);
  }
  .brand {
    position: absolute; right: 72px; top: 62px;
    display: flex; align-items: center; gap: 10px;
    font-family: "Outfit", sans-serif; font-weight: 600; font-size: 44px;
    letter-spacing: 1px; color: var(--white);
  }
  .brand-dot { width: 16px; height: 16px; border-radius: 50%; background: var(--orange); }
  .headline {
    position: absolute; left: 242px; top: 112px;
    font-family: "Oswald", sans-serif; font-weight: 700; font-size: 40px;
    line-height: 39px; text-transform: uppercase; letter-spacing: -1px; text-align: center;
  }
  .title-role {
    position: absolute; left: 366px; top: 196px; z-index: 3;
    font-family: "Oswald", sans-serif; font-weight: 600; font-size: 36px;
    color: var(--orange); letter-spacing: -0.5px;
  }
  .speaker-name {
    position: absolute; z-index: 2; font-family: "Barlow Condensed", sans-serif; font-weight: 800;
    color: var(--sky); letter-spacing: -5px; line-height: 1;
  }
  .speaker-first { left: 236px; top: 165px; font-size: 205px; }
  .speaker-last { left: 152px; top: 356px; font-size: 184px; letter-spacing: -5px; }
  .flame-art {
    position: absolute; left: 0; top: 380px; width: 180px; height: 380px;
    background: linear-gradient(180deg, rgba(247,147,30,0) 0%, var(--orange) 30%, #e8801a 100%);
    border-radius: 0 120px 60px 0;
  }
  .speaker-photo {
    position: absolute; z-index: 1; left: 0; top: 500px; width: 465px; height: 700px;
    background: linear-gradient(180deg, #3b4a63 0%, #3a78c9 40%, #2f68b8 100%);
    border-radius: 180px 180px 0 0;
  }
  .schedule { position: absolute; z-index: 3; left: 468px; top: 525px; width: 375px; }
  .session { position: relative; height: 81px; margin-bottom: 11px; }
  .session-bar {
    position: absolute; left: 30px; right: 0; top: 0; bottom: 0;
    background: var(--bar); border-radius: 6px;
  }
  .session-icon {
    position: absolute; left: 0; top: 1px; width: 79px; height: 79px;
    border-radius: 50%; background: var(--orange);
    display: flex; align-items: center; justify-content: center;
  }
  .session-text {
    position: absolute; left: 88px; top: 2px;
    font-family: "Oswald", sans-serif; font-weight: 600; letter-spacing: -0.8px;
  }
  .session-day { font-size: 28px; line-height: 38px; white-space: nowrap; }
  .session-time { font-size: 26px; line-height: 36px; display: flex; align-items: center; gap: 6px; }
  .app-note {
    position: absolute; left: 584px; top: 800px;
    font-size: 16px; line-height: 21px; font-weight: 400;
  }
  .app-badge {
    position: absolute; left: 496px; top: 868px; width: 235px; height: 83px;
    background: var(--white); border-radius: 8px;
    display: flex; align-items: center; justify-content: center;
    font-weight: 600; font-size: 40px; color: var(--ink); letter-spacing: 1px;
  }
  .download-btn {
    position: absolute; left: 471px; top: 884px; width: 54px; height: 54px;
    border-radius: 50%; background: var(--sky);
    display: flex; align-items: center; justify-content: center;
  }
  .contact-bar {
    position: absolute; z-index: 3; left: 27px; top: 1028px; width: 786px; height: 80px;
    background: var(--navy-deep); border-radius: 8px;
  }
  .contact-item { position: absolute; display: flex; align-items: flex-start; gap: 6px; }
  .contact-phone { left: 25px; top: 10px; font-weight: 600; font-size: 22px; }
  .contact-mail { left: 25px; top: 48px; font-size: 16px; }
  .contact-address { left: 255px; top: 9px; font-size: 16px; line-height: 22px; }
  .contact-web { left: 255px; top: 55px; font-size: 16px; color: var(--orange); }
</style>
</head>
<body>
<main class="flyer">
  <div class="flame-art" role="img" aria-label="Orange flame decoration behind the speaker"></div>

  <div class="brand"><span class="brand-dot"></span>VESTRA</div>

  <h2 class="headline">The Voice of<br>The Lord Speaker</h2>
  <p class="title-role">PROPHET</p>
  <h1 class="speaker-name speaker-first">Samuel</h1>
  <p class="speaker-name speaker-last">Onani</p>

  <div class="speaker-photo" role="img" aria-label="Photo of the speaker in a blue blazer and grey turtleneck"></div>

  <section class="schedule">
    <div class="session">
      <div class="session-bar"></div>
      <div class="session-icon">
        <svg width="44" height="40" viewBox="0 0 44 40"><rect x="2" y="6" width="34" height="30" rx="3" fill="none" stroke="#fff" stroke-width="3"/><rect x="2" y="6" width="34" height="8" fill="#fff"/><path d="M9 3v7M18 3v7M27 3v7" stroke="#fff" stroke-width="3"/><path d="M8 19h6v5H8zM17 19h6v5h-6zM8 27h6v5H8z" fill="#fff"/><path d="M25 29l5 5 11-11" fill="none" stroke="#fff" stroke-width="4"/></svg>
      </div>
      <div class="session-text">
        <div class="session-day">Friday, December 26th</div>
        <div class="session-time"><svg width="24" height="26" viewBox="0 0 24 26"><circle cx="12" cy="15" r="9" fill="none" stroke="#fff" stroke-width="2.5"/><path d="M12 15V10M12 15l4 2M9 2h6M12 2v4" stroke="#fff" stroke-width="2.5"/></svg>6:30PM - 9:00PM</div>
      </div>
    </div>
    <div class="session">
      <div class="session-bar"></div>
      <div class="session-icon">
        <svg width="44" height="40" viewBox="0 0 44 40"><rect x="2" y="6" width="34" height="30" rx="3" fill="none" stroke="#fff" stroke-width="3"/><rect x="2" y="6" width="34" height="8" fill="#fff"/><path d="M9 3v7M18 3v7M27 3v7" stroke="#fff" stroke-width="3"/><path d="M8 19h6v5H8zM17 19h6v5h-6zM8 27h6v5H8z" fill="#fff"/><path d="M25 29l5 5 11-11" fill="none" stroke="#fff" stroke-width="4"/></svg>
      </div>
      <div class="session-text">
        <div class="session-day">Saturday, December 27th</div>
        <div class="session-time"><svg width="24" height="26" viewBox="0 0 24 26"><circle cx="12" cy="15" r="9" fill="none" stroke="#fff" stroke-width="2.5"/><path d="M12 15V10M12 15l4 2M9 2h6M12 2v4" stroke="#fff" stroke-width="2.5"/></svg>5:30PM - 8:00PM</div>
      </div>
    </div>
    <div class="session">
      <div class="session-bar"></div>
      <div class="session-icon">
        <svg width="44" height="40" viewBox="0 0 44 40"><rect x="2" y="6" width="34" height="30" rx="3" fill="none" stroke="#fff" stroke-width="3"/><rect x="2" y="6" width="34" height="8" fill="#fff"/><path d="M9 3v7M18 3v7M27 3v7" stroke="#fff" stroke-width="3"/><path d="M8 19h6v5H8zM17 19h6v5h-6zM8 27h6v5H8z" fill="#fff"/><path d="M25 29l5 5 11-11" fill="none" stroke="#fff" stroke-width="4"/></svg>
      </div>
      <div class="session-text">
        <div class="session-day">Sunday, December 29th</div>
        <div class="session-time"><svg width="24" height="26" viewBox="0 0 24 26"><circle cx="12" cy="15" r="9" fill="none" stroke="#fff" stroke-width="2.5"/><path d="M12 15V10M12 15l4 2M9 2h6M12 2v4" stroke="#fff" stroke-width="2.5"/></svg>4:30PM - 7:00PM</div>
      </div>
    </div>
  </section>

  <p class="app-note">Download the<br>VESTRA App to Stay<br>updated on the event</p>
  <div class="app-badge">VESTRA</div>
  <div class="download-btn">
    <svg width="24" height="24" viewBox="0 0 24 24"><path d="M12 3v12M7 10l5 5 5-5M4 17v4h16v-4" fill="none" stroke="#fff" stroke-width="2.5"/></svg>
  </div>

  <footer class="contact-bar">
    <div class="contact-item contact-phone">
      <svg width="20" height="22" viewBox="0 0 24 24"><path d="M6 2l4 5-2 3c1 3 3 5 6 6l3-2 5 4-3 4C10 22 2 14 2 5z" fill="#fff"/></svg>555 014 2290
    </div>
    <div class="contact-item contact-mail">
      <svg width="20" height="16" viewBox="0 0 20 16"><rect x="1" y="1" width="18" height="14" fill="none" stroke="#fff" stroke-width="2"/><path d="M1 1l9 8 9-8" fill="none" stroke="#fff" stroke-width="2"/></svg>hello@vestra.org
    </div>
    <div class="contact-item contact-address">
      <svg width="14" height="20" viewBox="0 0 14 20"><path d="M7 1a6 6 0 0 1 6 6c0 5-6 12-6 12S1 12 1 7a6 6 0 0 1 6-6z" fill="#fff"/><circle cx="7" cy="7" r="2.2" fill="#141a36"/></svg>
      <span>The Harbor Lane Arts Hall 120 Millbrook<br>Street Fairhaven, Maine 04010</span>
    </div>
    <div class="contact-item contact-web">
      <svg width="18" height="18" viewBox="0 0 20 20"><circle cx="10" cy="10" r="8" fill="none" stroke="#fff" stroke-width="1.8"/><ellipse cx="10" cy="10" rx="3.5" ry="8" fill="none" stroke="#fff" stroke-width="1.8"/><path d="M2 10h16" stroke="#fff" stroke-width="1.8"/></svg>www.vestra.org
    </div>
  </footer>
</main>
</body>
</html>
```